A small boutique Accounting and Mortgage Broking firm needs a business card design

Torvel is a Brisbane based boutique accounting and mortgage broking firm. We offer a range of extensive financial services like accounting, tax consulting, book-keeping and mortgage broking.
We need a business card that stands out. The content can stay as it is on the existing card unless you recommend us to change anything on it for a better design.
Please remove the mobile number and give us a suitable format to change the details like email address and name.
Contact Information for Business Card
Dilan Karodi
Torvel Group Pty Ltd
3/412 Wendle Rd Salisbury QLD 4107
PO Box 829 Salisbury QLD 4107
T 07 3184 5526
F 07 3952 1873
E dkarodi@torvel-example.net.au
Accountants Tax Agents, Mortgage Brokers
www.torvel-example.net.au

```html
<!DOCTYPE html>
<html lang="en">
<head>
<meta charset="utf-8">
<title>Torvel Business Card</title>
<link rel="stylesheet" href="https://fonts.googleapis.com/css2?family=Lato:wght@300;400;700;900&display=swap">
<style>
  :root {
    --backdrop: #3a3a3c;
    --card-white: #ffffff;
    --brand-green: #7cc242;
    --brand-green-dark: #5fa62c;
    --tab-grey: #4a4a4c;
    --ink-navy: #1f1c5c;
    --ink-grey: #3d3d3f;
  }
  html, body {
    margin: 0;
    padding: 0;
    width: 1200px;
    height: 1023px;
    overflow: hidden;
    background: var(--backdrop);
    font-family: "Lato", Arial, sans-serif;
  }
  .stage { position: relative; width: 1200px; height: 1023px; }
  .card {
    position: absolute;
    left: 260px;
    width: 680px;
    height: 400px;
    border-radius: 28px;
    overflow: hidden;
    box-shadow: 0 10px 30px rgba(0,0,0,0.45);
  }
  .card--front { top: 80px; background: var(--card-white); }
  .card--back {
    top: 540px;
    background: radial-gradient(circle at 40% 45%, #8fd052 0%, var(--brand-green) 45%, var(--brand-green-dark) 100%);
  }
  .tab { position: absolute; width: 48px; height: 22px; }
  .tab--green { background: var(--brand-green); top: 0; right: 150px; }
  .tab--grey-bottom { background: var(--tab-grey); bottom: 0; left: 30px; }
  .tab--grey-top { background: var(--tab-grey); top: 0; right: 40px; }

  .brand { position: absolute; left: 40px; top: 190px; }
  .brand__row { display: flex; align-items: center; gap: 12px; }
  .brand__dot { width: 46px; height: 46px; border-radius: 50%; background: var(--ink-grey); }
  .brand__name {
    font-weight: 900;
    font-size: 54px;
    color: var(--ink-grey);
    letter-spacing: -1px;
    line-height: 1;
  }
  .brand__tagline {
    margin-top: 10px;
    font-size: 21px;
    font-weight: 300;
    letter-spacing: 1.5px;
    color: var(--ink-grey);
  }

  .person { position: absolute; right: 40px; top: 42px; text-align: right; }
  .person__name { font-size: 30px; color: var(--ink-navy); line-height: 1.1; }
  .person__role { font-size: 24px; color: var(--brand-green); line-height: 1.1; }

  .contacts { position: absolute; right: 36px; top: 150px; list-style: none; margin: 0; padding: 0; }
  .contacts__item {
    display: flex;
    justify-content: flex-end;
    align-items: center;
    gap: 12px;
    font-size: 16px;
    color: var(--ink-grey);
    height: 28px;
  }
  .contacts__icon { width: 16px; height: 16px; flex: none; }

  .address {
    position: absolute;
    left: 110px;
    bottom: 36px;
    font-size: 15px;
    color: var(--ink-grey);
    line-height: 1.35;
  }
  .address__company { font-weight: 700; }

  .services {
    position: absolute;
    right: 44px;
    top: 70px;
    text-align: right;
    color: #ffffff;
    font-size: 24px;
    font-weight: 400;
    letter-spacing: 1px;
    line-height: 1.35;
    text-transform: uppercase;
    list-style: none;
    margin: 0; padding: 0;
  }
</style>
</head>
<body>
<main class="stage">
  <section class="card card--front" aria-label="Business card front">
    <div class="tab tab--green"></div>
    <div class="tab tab--grey-bottom"></div>

    <div class="brand">
      <div class="brand__row">
        <div class="brand__dot"></div>
        <span class="brand__name">torvel</span>
      </div>
      <div class="brand__tagline">CLARITY. CARE. PROGRESS.</div>
    </div>

    <div class="person">
      <div class="person__name">Dilan Karodi</div>
      <div class="person__role">Director</div>
    </div>

    <ul class="contacts">
      <li class="contacts__item">07 3184 5526
        <svg class="contacts__icon" viewBox="0 0 16 16"><path fill="#7cc242" d="M3 1.5l2.5-.5 1.5 3.5-1.8 1.2a9 9 0 0 0 5 5l1.2-1.8 3.5 1.5-.5 2.5c-.3.8-1 1.2-1.9 1.1C6.6 13.5 2.5 9.4 1.9 3.4 1.8 2.5 2.2 1.8 3 1.5z"/></svg>
      </li>
      <li class="contacts__item">07 3952 1873
        <svg class="contacts__icon" viewBox="0 0 16 16"><rect x="4" y="1" width="8" height="5" fill="#7cc242"/><rect x="1" y="6" width="14" height="7" rx="1.5" fill="#7cc242"/><rect x="4" y="10" width="8" height="5" fill="#fff" stroke="#7cc242" stroke-width="1.2"/></svg>
      </li>
      <li class="contacts__item">dkarodi@torvel-example.net.au
        <svg class="contacts__icon" viewBox="0 0 16 16"><rect x="1" y="3" width="14" height="10" rx="1" fill="#7cc242"/><path d="M1.5 3.8L8 9l6.5-5.2" fill="none" stroke="#fff" stroke-width="1.2"/></svg>
      </li>
      <li class="contacts__item">www.torvel-example.net.au
        <svg class="contacts__icon" viewBox="0 0 16 16"><circle cx="8" cy="8" r="7" fill="#7cc242"/><g fill="none" stroke="#fff" stroke-width="1"><ellipse cx="8" cy="8" rx="3" ry="7"/><path d="M1 8h14M2.5 4.5h11M2.5 11.5h11"/></g></svg>
      </li>
    </ul>

    <div class="address">
      <div class="address__company">Torvel Group Pty Ltd</div>
      <div>3/412 Wendle Rd Kelbrook QLD 4199</div>
      <div>PO Box 829 Kelbrook QLD 4199</div>
    </div>
  </section>

  <section class="card card--back" aria-label="Business card back">
    <div class="tab tab--grey-top"></div>
    <ul class="services">
      <li>Accountants</li>
      <li>Tax Agent</li>
      <li>Book-Keepwers</li>
      <li>Mortgage Brokers</li>
    </ul>
  </section>
</main>
</body>
</html>
```